Cyber Security firm working in the Financial Services sector needs a brochure

We need a brochure covering our products and offerings. We work exclusively with Independent Broker Dealers, their Reps and RIAs in the US. We help them keep their computers secure and compliant with applicable regulations and policies. Have attached samples of our logo an descriptions of our products and services.

Target Market(s)

Financial Institutions and Financial Advisors

Industry/Entity Type

Financial Service

```html
<!DOCTYPE html>
<html lang="en">
<head>
<meta charset="utf-8">
<title>Cyber Security Solutions – Ironvale Secure</title>
<link rel="stylesheet" href="https://fonts.googleapis.com/css2?family=Ubuntu:wght@500;700&family=Open+Sans:wght@400;600&display=swap">
<style>
  :root {
    --navy: #1c3f91;
    --blue: #2b8ad6;
    --mist: #e2e7ed;
    --backdrop: #e9e9e9;
    --paper: #ffffff;
    --ink: #5a5f66;
    --ink-soft: #7b8189;
  }
  * { box-sizing: border-box; margin: 0; padding: 0; }
  html, body { width: 1200px; height: 960px; overflow: hidden; }
  body {
    background: var(--backdrop);
    font-family: "Open Sans", Arial, sans-serif;
    color: var(--ink);
  }
  .flyer {
    position: absolute;
    left: 250px; top: 27px;
    width: 700px; height: 906px;
    background: var(--paper);
    box-shadow: 0 6px 24px rgba(0,0,0,.12);
    overflow: hidden;
  }
  .flyer__shapes { position: absolute; inset: 0; }
  .brand {
    position: absolute; right: 44px; top: 30px;
    display: flex; align-items: center; gap: 8px;
    font-family: "Ubuntu", sans-serif; font-weight: 700;
    font-size: 20px; color: var(--navy);
  }
  .brand__dot { width: 12px; height: 12px; background: var(--navy); border-radius: 50%; }
  .title {
    position: absolute; left: 40px; top: 92px;
    font-family: "Ubuntu", sans-serif; font-weight: 700;
    font-size: 31px; color: var(--navy); letter-spacing: -.2px;
  }
  .hero {
    position: absolute; left: 0; top: 140px; width: 700px; height: 220px;
    background: linear-gradient(100deg, #3c4a5c 0%, #6f8398 35%, #b8cde0 60%, #7d90a6 100%);
  }
  .content {
    position: absolute; left: 0; top: 372px; width: 700px;
  }
  .intro {
    background: var(--mist);
    padding: 14px 40px 16px;
    font-size: 12px; line-height: 1.55; color: var(--ink-soft);
  }
  .services {
    display: grid;
    grid-template-columns: 340px 1fr;
    column-gap: 25px;
    row-gap: 14px;
    padding: 18px 40px 0;
  }
  .section--wide { grid-column: 1 / -1; }
  .section__head {
    font-family: "Ubuntu", sans-serif; font-weight: 700;
    font-size: 17px; line-height: 1.2; color: var(--navy); text-transform: uppercase;
    margin-bottom: 5px;
  }
  .section__body { font-size: 9.2px; line-height: 1.5; color: var(--ink); }
  .web {
    position: absolute; right: 40px; bottom: 30px;
    font-family: "Ubuntu", sans-serif; font-weight: 700;
    font-size: 14px; color: #fff; letter-spacing: .5px;
  }
</style>
</head>
<body>
<main class="flyer">
  <svg class="flyer__shapes" width="700" height="906" viewBox="0 0 700 906" aria-hidden="true">
    <polygon points="470,112 700,112 700,122 462,122" fill="var(--navy)"/>
    <polygon points="485,126 700,126 700,140 475,140" fill="var(--blue)"/>
    <polygon points="0,360 300,360 290,372 0,372" fill="var(--navy)"/>
    <polygon points="300,360 700,360 700,368 292,368" fill="var(--blue)"/>
    <polygon points="420,860 700,830 700,906 400,906" fill="var(--navy)"/>
    <polygon points="405,852 700,820 700,826 410,858" fill="var(--blue)"/>
  </svg>

  <div class="brand"><span class="brand__dot"></span>Ironvale Secure</div>
  <h1 class="title">Cyber Security Solutions</h1>

  <div class="hero" role="img" aria-label="Photo of a businessman touching a glowing padlock icon among streams of binary code"></div>

  <div class="content">
    <p class="intro">Ironvale Secure provides Computer Security support and services to the Broker Dealer and Independent Advisor community. We have been providing these services for over eight years and our team has decades of experience in the Financial Services sector. We currently support, monitor and inspect thousands of Advisors and their devices across multiple Broker Dealers and RIAs. Below is a list of our most popular services.</p>

    <div class="services">
      <section class="section section--wide">
        <h2 class="section__head">Managed Backup</h2>
        <p class="section__body">We partner with Carrow owned VaultLine Pro to provide backup services. This provides encrypted transmission and storage in SSAE 16 audited and ISO 27001 certified facilities for your back-up needs. We help you configure the back-ups, monitor them on a daily basis and are there to help if you need to do any restores. Price $1 per GB per month.</p>
      </section>

      <section class="section section--wide">
        <h2 class="section__head">Managed Anti-Virus</h2>
        <p class="section__body">Correctly functioning and up-to-date Anti-Virus (AV) software is a requirement for all computers connected to the internet. With only one or two computers it is relatively easy to stay on top of the situation. However, once you get more than a couple of computers and users knowing their condition becomes more difficult without centralized reporting and monitoring. Our managed AV solution provides a centralized portal for monitoring and reporting. We are notified of any issues, whether it's a virus detected or an issue with the AV itself. This software and service is available for $52 per user per year with a one time set up fee of $25 per device. The advantage of the per user fee is, if a user has both a desktop and a laptop, both will be covered for the $52 per year.</p>
      </section>

      <section class="section">
        <h2 class="section__head">Managed Software Patching</h2>
        <p class="section__body">Keeping computers up-to-date with all critical security patches is an important component in protecting your infrastructure. An effective Patch Management strategy requires timely application of patches. Our patching functions in a closed loop environment. We push the necessary patches to the computers and then use our monitoring system at the device level to verify all have been successfully applied. This solution is quite effective for distributed environments with limited local cyber security expertise as well as small offices which prefer to outsource this requirement. Price $3.99 per month per computer. Requires Computer Security Monitoring.</p>
      </section>

      <section class="section">
        <h2 class="section__head">Whole Disk Encryption</h2>
        <p class="section__body">We remotely access your computer and perform whole disk encryption as required by your Broker Dealer. We can also help you select the most appropriate encryption methodology for your specific environment. Pricing from $95 per computer.</p>
      </section>
    </div>
  </div>

  <div class="web">www.ironvalesecure.com</div>
</main>
</body>
</html>
```